Labels for probiotic care products as Body Cream, Shower gel, Hand soap, ....

We are a starting a business in Flanders Belgium. We are looking for a label for care products, based on probiotics or good bacterie. We are looking for a fresh design that attracts people who wants a good product, based on naturally components. The products make that the microflora of the skin becomes and remains natural. The label must we be adaptive on bottles of 15 cm height to 8 cm height and a width of 4,5 cm. The brand name is KOLA EMU (beautiful skin in Hawaiian) or maybe just KOLA.

Industry/Entity Type

Business

Colors

Designer to choose colors to be used in the design.

Requirements
Must have
• somewhere the text "Probiotic Skin Care"
• I also have to tell that the bottles are white.
Nice to have
• I uploaded the 9 existing labels, but I want a totally new one, because the labels of our cleaning products are the same. I also uploaded a mood bord of labels I like.

```html
<!DOCTYPE html>
<html lang="nl">
<head>
<meta charset="utf-8">
<title>KOLA EMU – Probiotic Skin Repair label</title>
<link rel="stylesheet" href="https://fonts.googleapis.com/css2?family=Montserrat:wght@400;600;700&family=Josefin+Sans:wght@300;400;600&family=Oswald:wght@300;400&display=swap">
<style>
  :root {
    --backdrop: #eeeeee;
    --label-white: #ffffff;
    --label-shade: #f1f1f1;
    --brand-green: #8fae2c;
    --brand-green-dark: #7a9a1f;
    --brand-green-light: #c9d99a;
    --type-grey: #8c8c8c;
    --type-dark: #2b2b2b;
    --name-dark: #4a5a1a;
    --info-band: #dadada;
    --pattern-grey: #e6e6e6;
  }
  * { box-sizing: border-box; margin: 0; padding: 0; }
  html, body { width: 900px; height: 1200px; overflow: hidden; }
  body { background: var(--backdrop); position: relative; }

  .label {
    position: absolute; left: 180px; top: 48px;
    width: 540px; height: 1105px;
    background: linear-gradient(90deg, var(--label-shade) 0%, var(--label-white) 20%, var(--label-white) 80%, var(--label-shade) 100%);
    overflow: hidden;
  }
  .leaf-band {
    position: absolute; top: 0; height: 104px;
    background: linear-gradient(135deg, var(--label-white) 0%, var(--brand-green-light) 45%, var(--label-white) 60%, var(--brand-green-light) 100%);
  }
  .leaf-band--left { left: 0; width: 150px; }
  .leaf-band--right { right: 0; width: 146px; }

  .brand-tab {
    position: absolute; left: 150px; top: 0; width: 244px; height: 191px;
    background: linear-gradient(180deg, var(--brand-green) 0%, var(--brand-green-dark) 100%);
    display: flex; align-items: flex-end; justify-content: center; padding-bottom: 20px;
  }
  .brand-name {
    font-family: "Montserrat", sans-serif; font-weight: 700; font-size: 40px;
    color: var(--name-dark); letter-spacing: 0.5px;
  }
  .range-badge {
    position: absolute; left: 150px; top: 191px; width: 244px; height: 102px;
    background: var(--brand-green);
    border-radius: 0 0 122px 122px / 0 0 102px 102px;
    display: flex; justify-content: center; padding-top: 22px;
  }
  .range-name {
    font-family: "Josefin Sans", sans-serif; font-weight: 400; font-size: 29px;
    color: var(--label-white); letter-spacing: 0.5px;
  }

  .category {
    position: absolute; left: 0; width: 100%; top: 345px; text-align: center;
    font-family: "Josefin Sans", sans-serif; font-weight: 400; font-size: 40px;
    color: var(--brand-green);
  }
  .rule {
    position: absolute; left: 124px; width: 290px; height: 5px;
    background: var(--brand-green);
  }
  .rule--top { top: 400px; }
  .rule--bottom { top: 648px; }

  .product-title {
    position: absolute; left: 0; width: 100%; text-align: center;
    font-family: "Montserrat", sans-serif; font-weight: 600; color: var(--type-grey);
    line-height: 1;
  }
  .product-title--main { top: 415px; font-size: 146px; letter-spacing: 1px; }
  .product-title--sub { top: 568px; font-size: 82px; letter-spacing: 1px; }

  .tagline {
    position: absolute; left: 0; width: 100%; top: 690px; text-align: center;
    font-family: "Josefin Sans", sans-serif; color: var(--type-dark); line-height: 1.3;
  }
  .tagline__light { display: block; font-weight: 300; font-size: 34px; letter-spacing: 1px; }
  .tagline__bold { display: block; font-weight: 600; font-size: 34px; letter-spacing: 1px; }

  .microbe-field {
    position: absolute; left: 0; top: 770px; width: 100%; height: 218px;
    background: linear-gradient(180deg, var(--label-white) 0%, var(--pattern-grey) 100%);
  }
  .volume {
    position: absolute; left: 0; width: 100%; top: 868px; text-align: center;
    font-family: "Josefin Sans", sans-serif; font-weight: 600; font-size: 30px;
    color: var(--brand-green);
  }

  .info-band {
    position: absolute; left: 0; top: 988px; width: 100%; height: 95px;
    background: var(--info-band);
    padding: 30px 118px 0 122px;
  }
  .info-text {
    font-family: "Oswald", sans-serif; font-weight: 300; font-size: 12.5px;
    line-height: 1.35; color: var(--type-dark);
  }
  .base-stripe {
    position: absolute; left: 0; top: 1083px; width: 100%; height: 9px;
    background: var(--brand-green);
  }
</style>
</head>
<body>
  <main class="label">
    <div class="leaf-band leaf-band--left" role="img" aria-label="Line-drawn leaf and triangle pattern in green and white"></div>
    <div class="leaf-band leaf-band--right" role="img" aria-label="Line-drawn leaf and triangle pattern in green and white"></div>

    <div class="brand-tab"><span class="brand-name">KOLA EMU</span></div>
    <div class="range-badge"><span class="range-name">PROBIOTIC</span></div>

    <p class="category">Skin Care</p>
    <div class="rule rule--top"></div>
    <h1 class="product-title product-title--main">SKIN</h1>
    <h2 class="product-title product-title--sub">REPAIR</h2>
    <div class="rule rule--bottom"></div>

    <p class="tagline">
      <span class="tagline__light">BEAUTIFUL BY</span>
      <span class="tagline__bold">NATURE</span>
    </p>

    <div class="microbe-field" role="img" aria-label="Faint grey pattern of line-drawn microbes and bacteria"></div>
    <p class="volume">60ML</p>

    <div class="info-band">
      <p class="info-text">Een probiotische huidcrème, voor volwassenen en kinderen.<br>
      Dagelijks gebruik vormt een beschermende goede huidflora en<br>
      reinigt diep. Aanbrengen op een droge huid.</p>
    </div>
    <div class="base-stripe"></div>
  </main>
</body>
</html>
```